NZ First of it's kind solutions directory and marketplace for busy Mums needs a business card design

We need a business card design for our new nationwide business in NZ (long term plans to go global). We provide solutions to the everyday challenges that busy Mums face by connecting them with quality communities and suppliers of carefully selected, relevant products and services. We sell direct via our online marketplace. The final design should communicate our values of inclusivity, quality and smart solutions. Colours should incorporate our logo colour palette of #477077 and #6ba8b2. Our website is at https://www.brightnestly.com

Target Market(s)

busy Mums, Age 28 – 50, female, income over $100K, location main centres NZ primarily but NZ wide. Is likely juggling work or career with a young family. Probably had hobbies which have fallen by the wayside.
-Wants to succeed in her chosen career without compromising on family life
-to successfully juggle her career without feeling like she is compromising her children
- Is time poor, something always has to give and it’s generally her health (she’ll stay up late, get stressed)
- probably ex corporate or professional career. Has discretional income

Industry/Entity Type

Business

Contact Information for Business Card

Jodie Farnsworth, Founder, BrightNestly.com (Strapline Browse; Pick; Sorted), 48 Kowhai Terrace, Hillsborough, Auckland 1058, New Zealand. Mob: 021 437 518 Ph: +64 (0)9 584 7163

Font styles to use
Other font styles liked:
• Raleway, and/or Architects Daughter

Colors
00a990
33b8a4
86cfc6
cfeae6

Requirements
Must have
• the above details, streamline. the logo and colours associated with those logos
Should not have
• foil or metallic colours

```html
<!DOCTYPE html>
<html lang="en">
<head>
<meta charset="utf-8">
<title>BrightNestly – Business Card</title>
<link rel="stylesheet" href="https://fonts.googleapis.com/css2?family=Raleway:wght@300;400;600;700&family=Open+Sans:wght@400&display=swap">
<style>
  :root {
    --teal-dark: #477077;
    --teal-light: #6ba8b2;
    --paper: #ffffff;
    --ink: #3c5e64;
    --ink-soft: #4a4a4a;
    --backdrop: #c8c8c8;
    --icon-line: #8a9799;
  }
  html, body {
    margin: 0;
    padding: 0;
    width: 1053px;
    height: 1200px;
    overflow: hidden;
    background: var(--backdrop);
  }
  .canvas {
    position: relative;
    width: 1053px;
    height: 1200px;
  }
  .card {
    position: absolute;
    left: 96px;
    width: 860px;
    height: 516px;
    background: var(--paper);
    overflow: hidden;
    box-shadow: 0 10px 24px rgba(0,0,0,0.28), 0 2px 5px rgba(0,0,0,0.18);
  }
  .card--front { top: 60px; }
  .card--back  { top: 624px; }
  .card__waves {
    position: absolute;
    inset: 0;
    width: 860px;
    height: 516px;
  }
  .wave--light { fill: var(--teal-light); }
  .wave--dark  { fill: var(--teal-dark); }

  /* Brand lockup */
  .brand {
    position: absolute;
    display: flex;
    align-items: center;
    gap: 18px;
  }
  .brand__dot {
    width: 54px;
    height: 54px;
    border-radius: 50%;
    background: var(--teal-dark);
  }
  .brand__name {
    font-family: "Raleway", sans-serif;
    font-weight: 700;
    color: var(--teal-dark);
    letter-spacing: -0.5px;
    line-height: 1;
  }
  .card--front .brand { left: 44px; top: 50px; }
  .card--front .brand__name { font-size: 52px; }

  /* Contact list */
  .contacts {
    position: absolute;
    left: 40px;
    top: 206px;
    margin: 0;
    padding: 0;
    list-style: none;
    font-family: "Open Sans", sans-serif;
    font-size: 20px;
    color: var(--ink);
  }
  .contacts__item {
    display: flex;
    align-items: flex-start;
    gap: 16px;
    margin-bottom: 16px;
    line-height: 25px;
  }
  .contacts__icon {
    flex: none;
    width: 26px;
    height: 26px;
  }
  .contacts__icon circle { fill: none; stroke: var(--icon-line); stroke-width: 1.4; }
  .contacts__icon path { fill: none; stroke: var(--icon-line); stroke-width: 1.4; stroke-linecap: round; stroke-linejoin: round; }

  /* Person */
  .person {
    position: absolute;
    right: 44px;
    bottom: 58px;
    text-align: right;
    color: var(--paper);
    font-family: "Raleway", sans-serif;
  }
  .person__name {
    font-size: 38px;
    font-weight: 300;
    text-transform: uppercase;
    letter-spacing: 0.5px;
    line-height: 1.1;
  }
  .person__surname { font-weight: 600; }
  .person__role {
    font-size: 22px;
    font-weight: 400;
    text-transform: uppercase;
    letter-spacing: 1px;
    margin-top: 4px;
  }

  /* Back side */
  .card--back .brand {
    left: 0;
    right: 0;
    top: 190px;
    justify-content: center;
    gap: 22px;
  }
  .card--back .brand__dot { width: 64px; height: 64px; }
  .card--back .brand__name { font-size: 62px; }
  .web-address {
    position: absolute;
    left: 0;
    right: 0;
    top: 294px;
    text-align: center;
    font-family: "Raleway", sans-serif;
    font-size: 25px;
    font-weight: 400;
    letter-spacing: 0.32em;
    color: var(--ink-soft);
  }
</style>
</head>
<body>
<main class="canvas">

  <section class="card card--front" aria-label="Business card front">
    <svg class="card__waves" viewBox="0 0 860 516" aria-hidden="true">
      <path class="wave--light" d="M0,470 C240,482 420,346 560,236 C680,146 780,132 860,140 L860,516 L0,516 Z"/>
      <path class="wave--dark" d="M0,494 C250,506 430,372 575,262 C690,176 785,162 860,170 L860,516 L0,516 Z"/>
    </svg>

    <div class="brand">
      <span class="brand__dot"></span>
      <span class="brand__name">BrightNestly</span>
    </div>

    <ul class="contacts">
      <li class="contacts__item">
        <svg class="contacts__icon" viewBox="0 0 26 26" aria-hidden="true"><circle cx="13" cy="13" r="12"/><path d="M10,7 h6 v12 h-6 z M12,17 h2"/></svg>
        <span>021 437 518</span>
      </li>
      <li class="contacts__item">
        <svg class="contacts__icon" viewBox="0 0 26 26" aria-hidden="true"><circle cx="13" cy="13" r="12"/><path d="M9,7 l2.5,0 l1,3.5 l-1.8,1.3 c0.8,1.8 2,3 3.5,3.6 l1.3,-1.8 l3.5,1 l0,2.4 c-5,0.6 -10.5,-4.5 -10,-10 z"/></svg>
        <span>+64 (0)9 584 7163</span>
      </li>
      <li class="contacts__item">
        <svg class="contacts__icon" viewBox="0 0 26 26" aria-hidden="true"><circle cx="13" cy="13" r="12"/><path d="M13,20 c-3,-4 -5,-6.5 -5,-9 a5,5 0 0 1 10,0 c0,2.5 -2,5 -5,9 z M13,9.5 a1.5,1.5 0 1 0 0.01,0"/></svg>
        <span>48 Kowhai Terrace, Hillsborough, Auckland<br>1058, New Zealand</span>
      </li>
      <li class="contacts__item">
        <svg class="contacts__icon" viewBox="0 0 26 26" aria-hidden="true"><circle cx="13" cy="13" r="12"/><path d="M13,6 a7,7 0 1 0 0.01,0 M6,13 h14 M13,6 c-3,3.5 -3,10.5 0,14 M13,6 c3,3.5 3,10.5 0,14"/></svg>
        <span>BrightNestly.com</span>
      </li>
    </ul>

    <div class="person">
      <div class="person__name">Jodie <span class="person__surname">Farnsworth</span></div>
      <div class="person__role">Founder</div>
    </div>
  </section>

  <section class="card card--back" aria-label="Business card back">
    <svg class="card__waves" viewBox="0 0 860 516" aria-hidden="true">
      <path class="wave--light" d="M0,0 L860,0 L860,172 C700,140 560,70 380,62 C220,56 110,96 0,110 Z"/>
      <path class="wave--dark" d="M0,0 L860,0 L860,150 C700,118 560,48 380,40 C220,34 110,74 0,88 Z"/>
      <path class="wave--light" d="M0,346 C150,360 300,372 470,380 C650,388 770,416 860,442 L860,516 L0,516 Z"/>
      <path class="wave--dark" d="M0,370 C150,384 300,396 470,404 C650,412 770,440 860,466 L860,516 L0,516 Z"/>
    </svg>

    <div class="brand">
      <span class="brand__dot"></span>
      <span class="brand__name">BrightNestly</span>
    </div>
    <div class="web-address">BRIGHTNESTLY.COM</div>
  </section>

</main>
</body>
</html>
```